R & T Summit Construction Business Card ideas

We want a business card to represents our company in a way that looks professional but is also a business card that is unique!

Industry/Entity Type

Construction Company

Contact Information for Business Card

open to all design ideas, just want to be able to see different options to choose from in either color or grayscale.

Requirements
Must have
• Our names and phone numbers
• Nolan Pritchett 512-804-2271
• Curtis Hale 512-693-1804
• Business logo

```html
<!DOCTYPE html>
<html lang="en">
<head>
<meta charset="utf-8">
<title>R &amp; T Summit Construction – Business Card</title>
<link href="https://fonts.googleapis.com/css2?family=Montserrat:wght@400;500;700&display=swap" rel="stylesheet">
<style>
  :root {
    --bg: #e9e6e1;
    --card-white: #fbfbfb;
    --ink: #111111;
    --ink-soft: #555555;
    --rule: #8a8a8a;
    --paper-on-dark: #f2f2f2;
    --house-tone: #2a2a2a;
  }
  * { margin: 0; padding: 0; box-sizing: border-box; }
  html, body { width: 1200px; height: 1023px; overflow: hidden; }
  body {
    background: var(--bg);
    font-family: "Montserrat", sans-serif;
    color: var(--ink);
    position: relative;
  }
  .card {
    position: absolute;
    left: 325px;
    width: 550px;
    height: 314px;
    border-radius: 22px;
    overflow: hidden;
    box-shadow: 0 10px 28px rgba(0,0,0,.22);
  }
  .card--front { top: 150px; background: var(--card-white); }
  .card--back  { top: 560px; background: var(--ink); color: var(--paper-on-dark); }

  /* front */
  .front-wave { position: absolute; inset: 0; }
  .brand {
    position: absolute;
    font-weight: 500;
    letter-spacing: .06em;
    text-transform: uppercase;
  }
  .card--front .brand { top: 42px; left: 150px; font-size: 19px; color: var(--ink); }
  .brand-mark {
    display: inline-block; width: 12px; height: 12px;
    background: currentColor; margin-right: 10px; vertical-align: 1px;
  }
  .front-rule {
    position: absolute; top: 86px; left: 150px; width: 250px;
    border-top: 1px solid var(--rule);
  }
  .address {
    position: absolute; top: 112px; right: 150px;
    font-size: 11px; line-height: 1.55; color: var(--ink-soft); text-align: right;
  }
  .person { position: absolute; left: 40px; top: 190px; }
  .person__name { font-weight: 700; font-size: 17px; letter-spacing: .02em; text-transform: uppercase; }
  .person__title { font-size: 11.5px; color: var(--ink-soft); margin-top: 2px; }
  .name-dots {
    position: absolute; left: 230px; top: 203px; width: 110px;
    border-top: 2px dotted var(--ink-soft);
  }
  .contacts { position: absolute; left: 40px; top: 240px; list-style: none; font-size: 11.5px; color: var(--ink-soft); }
  .contacts li { display: flex; align-items: center; gap: 8px; height: 17px; }
  .contacts svg { width: 10px; height: 10px; fill: var(--ink); }

  /* back */
  .card--back .brand {
    top: 138px; left: 0; right: 0; text-align: center; font-size: 23px;
  }
  .back-rule {
    position: absolute; top: 176px; left: 165px; width: 220px;
    border-top: 1px solid var(--paper-on-dark);
  }
  .back-site {
    position: absolute; left: 0; right: 0; bottom: 26px;
    text-align: center; font-size: 12px; letter-spacing: .32em;
  }
  .back-line {
    position: absolute; bottom: 34px; height: 1px; width: 120px;
    background: var(--paper-on-dark); opacity: .8;
  }
  .back-line--left { left: 36px; }
  .back-line--right { right: 36px; }
</style>
</head>
<body>
  <section class="card card--front" aria-label="Business card front">
    <svg class="front-wave" viewBox="0 0 550 314" width="550" height="314" aria-hidden="true">
      <path d="M550 60 C470 70 460 140 430 200 C405 255 400 300 360 314 L550 314 Z" fill="#111"/>
      <path d="M550 74 C480 86 472 150 444 208 C420 258 414 300 378 314" fill="none" stroke="#fbfbfb" stroke-width="3"/>
    </svg>
    <div role="img" aria-label="Row of house rooftop silhouettes along the wave"
         style="position:absolute; right:20px; top:70px; width:95px; height:70px; background:var(--house-tone); border-radius:4px;"></div>
    <div class="brand"><span class="brand-mark"></span>R &amp; T Summit Construction</div>
    <div class="front-rule"></div>
    <p class="address">Ridgeline Rd 40, 78701,<br>Austin, Texas</p>
    <div class="person">
      <p class="person__name">Nolan Pritchett</p>
      <p class="person__title">Managing Director</p>
    </div>
    <div class="name-dots"></div>
    <ul class="contacts">
      <li><svg viewBox="0 0 10 10"><path d="M2 0h2l1 3-1.5 1a6 6 0 0 0 2.5 2.5L7 5l3 1v2a2 2 0 0 1-2 2A8 8 0 0 1 0 2a2 2 0 0 1 2-2z"/></svg>512-804-2271</li>
      <li><svg viewBox="0 0 10 10"><path d="M0 2h10v6H0z M0 2l5 3.5L10 2" stroke="#fbfbfb" stroke-width=".8"/></svg>office@rtsummitbuild.com</li>
      <li><svg viewBox="0 0 10 10"><circle cx="5" cy="5" r="5"/></svg>www.rtsummitbuild.com</li>
    </ul>
  </section>

  <section class="card card--back" aria-label="Business card back">
    <div class="brand"><span class="brand-mark"></span>R &amp; T Summit Construction</div>
    <div class="back-rule"></div>
    <span class="back-line back-line--left"></span>
    <p class="back-site">www.rtsummitbuild.com</p>
    <span class="back-line back-line--right"></span>
  </section>
</body>
</html>
```